Economic Book Cover

I need a book cover for a 5.5" x 8.5" paperback book that is 100 pages long. No title or words on the spine please, as the book is too thin to print on the spine. The title of the book is The Nine Harbor Lanterns. The subtitle is "The Patient Weave of Morning Light and Quiet Harbor Stones"
We'd like the cover to have a drawing of a dove offering an olive branch to a hundred dollar bill. You could use the attached illustration or create your own. The cover should be peaceful, hopeful, with cool colors.
The back cover should have the attached book description on it.
The authors name is Derek Halvorn and should be listed only on the front cover. No author's photo or description of the author need appear on the back cover, just the book description.
American voters

```html
<!DOCTYPE html>
<html lang="en">
<head>
<meta charset="utf-8">
<title>The Nine Harbor Lanterns — Book Cover</title>
<link rel="stylesheet" href="https://fonts.googleapis.com/css2?family=Fira+Sans+Condensed:ital,wght@0,400;0,500;0,700;1,700&family=Fira+Sans+Extra+Condensed:wght@600&display=swap">
<style>
  :root {
    --backdrop: #ecebe7;
    --paper: #ffffff;
    --sage: #a9c890;
    --sage-soft: #d7e6cb;
    --ink: #1c1c1c;
    --ink-soft: #2e2e2e;
    --title: #ffffff;
  }
  * { box-sizing: border-box; margin: 0; padding: 0; }
  html, body {
    width: 1200px; height: 1000px; overflow: hidden;
    background: var(--backdrop);
  }
  .canvas { position: relative; width: 1200px; height: 1000px; }
  .cover {
    position: absolute; top: 144px; width: 473px; height: 718px;
    background: var(--paper);
  }
  .cover--back {
    left: 111px;
    background: linear-gradient(to bottom, var(--paper) 0%, var(--paper) 44%, var(--sage) 100%);
  }
  .cover--front {
    left: 616px;
    background: linear-gradient(to bottom, var(--sage) 0%, var(--sage-soft) 30%, var(--paper) 62%, var(--paper) 100%);
  }
  .blurb {
    position: absolute; left: 59px; top: 145px; width: 360px;
    font-family: "Fira Sans Condensed", sans-serif;
    font-size: 12px; line-height: 26px; color: var(--ink-soft);
  }
  .blurb p + p { margin-top: 18px; }
  .blurb__title { font-weight: 700; font-style: italic; color: var(--ink); }
  .title {
    position: absolute; left: 0; right: 0; top: 66px; text-align: center;
    font-family: "Fira Sans Extra Condensed", sans-serif; font-weight: 600;
    font-size: 50px; line-height: 50px; letter-spacing: 1px; color: var(--title);
  }
  .subtitle {
    position: absolute; left: 0; right: 0; top: 172px; text-align: center;
    font-family: "Fira Sans Condensed", sans-serif; font-weight: 400;
    font-size: 15.5px; line-height: 27px; letter-spacing: 0.5px; color: var(--ink-soft);
  }
  .artwork {
    position: absolute; left: 76px; top: 298px; width: 324px; height: 280px;
    border-radius: 12px;
    background: radial-gradient(ellipse at 60% 45%, #f3f6ef 0%, #cfe0c0 55%, #a9c890 100%);
  }
  .author {
    position: absolute; left: 0; right: 0; top: 648px; text-align: center;
    font-family: "Fira Sans Condensed", sans-serif; font-weight: 500;
    font-size: 16px; letter-spacing: 1px; color: var(--ink);
  }
</style>
</head>
<body>
<main class="canvas">
  <section class="cover cover--back" aria-label="Back cover">
    <div class="blurb">
      <p><span class="blurb__title">The Nine Harbor Lanterns</span> is a practical guide to the liberation of our nation's economic woes. Halvorn introduces an entirely new way of looking at our economy that revolutionizes our financial system, producing an unprecedented level abundance for all.</p>
      <p>If we follow the Nine Harbor Lanterns, we can eliminate income taxes, balance our budget, and pay off the national debt. Our economy will boom, our citizens will prosper, and America will achieve a higher level of international prominence than ever before.</p>
    </div>
  </section>

  <section class="cover cover--front" aria-label="Front cover">
    <h1 class="title">THE NINE HARBOR<br>LANTERNS</h1>
    <p class="subtitle">The Patient Weave of Morning Light<br>and Quiet Harbor Stones</p>
    <div class="artwork" role="img" aria-label="Illustration of a white dove carrying an olive branch and a hundred dollar bill"></div>
    <p class="author">DEREK HALVORN</p>
  </section>
</main>
</body>
</html>
```